Business Card Design Project

We need a business card design for a new boutique consulting company, LumaConsulting. Our new logo has just been designed and we are looking for simple, clean looking business cards. Logo attached

Industry/Entity Type

Boutique

Requirements
Must have
• There must be room for each card to have the following details:
Name
Title
Address - 2 lines
Phone number
Email address
Website address

Nice to have
• May have something on the back of the buisness card - emphasing the word "Luma".

```html
<!DOCTYPE html>
<html lang="en">
<head>
<meta charset="utf-8">
<title>LumaConsulting Business Cards</title>
<link rel="stylesheet" href="https://fonts.googleapis.com/css2?family=Source+Sans+3:wght@400;600&display=swap">
<style>
  :root {
    --backdrop: #d5d6d8;
    --card: #ffffff;
    --brand-blue: #0a5499;
    --brand-yellow: #fff200;
    --wordmark-grey: #8b8c8e;
    --text-light: #ffffff;
  }
  * { margin: 0; padding: 0; box-sizing: border-box; }
  html, body {
    width: 1200px;
    height: 900px;
    overflow: hidden;
    background: var(--backdrop);
    font-family: "Source Sans 3", "Myriad Pro", Arial, sans-serif;
  }
  .canvas { position: relative; width: 1200px; height: 900px; }
  .card {
    position: absolute;
    left: 274px;
    width: 648px;
    height: 376px;
    background: var(--card);
  }
  .card--back { top: 40px; }
  .card--front { top: 484px; }
  .card-shapes { position: absolute; inset: 0; }
  .panel-blue { fill: var(--brand-blue); }
  .panel-yellow { fill: var(--brand-yellow); }
  .wordmark {
    position: absolute;
    color: var(--wordmark-grey);
    font-weight: 400;
    letter-spacing: -1px;
    line-height: 1;
    white-space: nowrap;
  }
  .card--back .wordmark { left: 162px; top: 278px; font-size: 56px; }
  .card--front .wordmark { left: 190px; top: 284px; font-size: 46px; }
  .contact { position: absolute; color: var(--text-light); line-height: 1; white-space: nowrap; }
  .employee-name { left: 66px; top: 56px; font-size: 29px; font-weight: 400; }
  .job-title { left: 190px; top: 96px; font-size: 24px; }
  .address { left: 396px; top: 54px; font-size: 20px; line-height: 30px; font-weight: 600; }
  .online { left: 0; width: 648px; top: 176px; text-align: center; font-size: 20px; line-height: 28px; padding-left: 40px; }
</style>
</head>
<body>
<div class="canvas">
  <section class="card card--back" aria-label="Card back">
    <svg class="card-shapes" width="648" height="376" viewBox="0 0 648 376">
      <path class="panel-blue" d="M38,30 H612 Q630,30 630,48 V222 Q630,240 612,240 H82 Q64,226 50,206 Q36,188 20,180 V48 Q20,30 38,30 Z"/>
      <path class="panel-yellow" d="M82,260 H612 Q630,260 630,278 V334 Q630,352 612,352 H38 Q20,352 20,334 V296 Q40,290 52,276 Q66,260 82,260 Z"/>
    </svg>
    <div class="wordmark">LumaConsulting</div>
  </section>

  <section class="card card--front" aria-label="Card front">
    <svg class="card-shapes" width="648" height="376" viewBox="0 0 648 376">
      <path class="panel-blue" d="M38,30 H612 Q630,30 630,48 V222 Q630,240 612,240 H82 Q64,226 50,206 Q36,188 20,180 V48 Q20,30 38,30 Z"/>
      <path class="panel-yellow" d="M82,260 H612 Q630,260 630,278 V334 Q630,352 612,352 H38 Q20,352 20,334 V296 Q40,290 52,276 Q66,260 82,260 Z"/>
    </svg>
    <p class="contact employee-name">employee name</p>
    <p class="contact job-title">job title</p>
    <p class="contact address">Address 1<br>Address 2<br>Phone: (07) 5550 1234</p>
    <p class="contact online">email: sales@lumaconsulting.com<br>web: www.lumaconsulting.com</p>
    <div class="wordmark">LumaConsulting</div>
  </section>
</div>
</body>
</html>
```